Our Kitchen Pantry is an online food market place that connects foodies who make or grow great food with

We would like a 1/2 A4 page size flyer in landscape to promote our new business. We would like to encourage new home foodies to sign up for a membership on our website www.ourkitchenpantrynz.co.nz and we would like customers who are looking for great food in their local community to search our website for their closest home foodie and support a neighbour who is growing or producing creative food locally

Target Market(s)

Creative food lovers

Industry/Entity Type

Landscape

Colors
acd037
f78f20
33b8a4

Requirements
Must have
• Food images and look groovy
• Must be easy to read and stand out on a notice board
• Website address www.ourkitchenpantrynz.co.nz
Nice to have
• We wish to use this flyer in multiple locations and wish to put in different contact details prior to printing

```html
<!DOCTYPE html>
<html lang="en">
<head>
<meta charset="utf-8">
<title>Our Kitchen Pantry – Flyer</title>
<link href="https://fonts.googleapis.com/css2?family=Pacifico&family=Roboto:wght@400;500;700;900&display=swap" rel="stylesheet">
<style>
  :root {
    --page: #e9e9e6;
    --sun-light: #ffe600;
    --sun-mid: #fbc312;
    --sun-deep: #f78f20;
    --lime: #acd037;
    --lime-dark: #8db82a;
    --leaf: #2e8b2e;
    --leaf-deep: #237a25;
    --berry: #e8192c;
    --ink: #1e1e1e;
    --white: #ffffff;
    --kraft: #c4a57c;
    --brown: #4a2a12;
    --fruit-a: #f4b43a;
    --fruit-b: #c9283a;
    --fruit-c: #6d8b3c;
  }
  * { margin: 0; padding: 0; box-sizing: border-box; }
  html, body {
    width: 1200px; height: 900px; overflow: hidden;
    background: var(--page);
    font-family: "Roboto", Arial, sans-serif;
  }
  .flyer {
    position: absolute; left: 78px; top: 78px;
    width: 1044px; height: 744px; overflow: hidden;
    background: radial-gradient(ellipse at 62% 30%, var(--sun-light) 0%, var(--sun-mid) 45%, var(--sun-deep) 100%);
    box-shadow: 0 10px 28px rgba(0,0,0,.25);
  }
  .flyer-shapes { position: absolute; inset: 0; }
  .script {
    position: absolute; font-family: "Pacifico", cursive;
    color: var(--leaf); line-height: 1; white-space: nowrap;
    -webkit-text-stroke: 0;
    text-shadow:
      3px 0 0 var(--white), -3px 0 0 var(--white), 0 3px 0 var(--white), 0 -3px 0 var(--white),
      2px 2px 0 var(--white), -2px -2px 0 var(--white), 2px -2px 0 var(--white), -2px 2px 0 var(--white),
      4px 5px 6px rgba(0,0,0,.35);
  }
  .headline-top { left: 368px; top: 20px; font-size: 64px; }
  .headline-foodie { left: 40px; top: 480px; font-size: 72px; }

  .brand {
    position: absolute; left: 50px; top: 42px; width: 260px; height: 260px;
    display: flex; align-items: center; justify-content: center; text-align: center;
  }
  .brand-circle {
    position: absolute; inset: 0; border-radius: 50%;
    background: var(--kraft); border: 6px solid var(--white);
    box-shadow: 3px 5px 10px rgba(0,0,0,.3);
  }
  .brand-name {
    position: relative; font-weight: 900; font-size: 40px; line-height: 1.05;
    color: var(--brown); text-transform: uppercase; width: 210px;
  }

  .pitch { position: absolute; right: 41px; text-align: right; text-transform: uppercase; }
  .pitch-lead { top: 184px; font-size: 21px; font-weight: 700; color: var(--ink); }
  .pitch-big { top: 214px; font-size: 44px; font-weight: 500; color: var(--berry); letter-spacing: .5px; }
  .pitch-tail { top: 266px; font-size: 18px; font-weight: 700; color: var(--ink); }

  .about {
    position: absolute; right: 41px; top: 356px; width: 330px;
    text-align: right; font-size: 15.5px; line-height: 22.5px; color: var(--ink);
  }
  .info { position: absolute; right: 41px; top: 510px; text-align: right; }
  .info-label { font-size: 19px; font-weight: 500; color: var(--berry); text-transform: uppercase; }
  .info-web { font-size: 15px; font-weight: 700; color: var(--ink); margin-top: 6px; }

  .sell { position: absolute; left: 40px; top: 644px; text-transform: uppercase; }
  .sell-lead {
    font-size: 24px; font-weight: 500; color: var(--berry);
    text-shadow: 2px 0 0 var(--white), -2px 0 0 var(--white), 0 2px 0 var(--white), 0 -2px 0 var(--white);
  }
  .sell-tail { font-size: 20px; font-weight: 700; color: var(--ink); margin-top: 10px; }

  .contact { position: absolute; left: 822px; top: 646px; }
  .contact-label {
    font-size: 20px; font-weight: 500; color: var(--ink); text-transform: uppercase;
    text-shadow: 1px 0 0 var(--white), -1px 0 0 var(--white), 0 1px 0 var(--white), 0 -1px 0 var(--white);
  }
  .contact-phone {
    font-size: 27px; font-weight: 500; color: var(--berry); margin-top: 6px;
    text-shadow: 2px 0 0 var(--white), -2px 0 0 var(--white), 0 2px 0 var(--white), 0 -2px 0 var(--white);
  }
</style>
</head>
<body>
<div class="flyer">
  <svg class="flyer-shapes" width="1044" height="744" viewBox="0 0 1044 744">
    <defs>
      <linearGradient id="fruitTones" x1="0" y1="0" x2="1" y2="1">
        <stop offset="0" stop-color="#9aa3a8"/>
        <stop offset=".3" stop-color="var(--fruit-a)"/>
        <stop offset=".6" stop-color="var(--fruit-b)"/>
        <stop offset=".85" stop-color="var(--fruit-c)"/>
        <stop offset="1" stop-color="var(--fruit-a)"/>
      </linearGradient>
    </defs>
    <!-- top-left lime sweep -->
    <path d="M0 64 L360 150 L360 170 L0 90 Z" fill="var(--white)"/>
    <path d="M0 70 L360 156 L360 166 L0 84 Z" fill="var(--lime)"/>
    <!-- food photo area -->
    <path d="M0 84 L300 150 Q520 260 720 612 L0 612 Z" fill="url(#fruitTones)" role="img" aria-label="Photo of a colourful fresh fruit tart with berries, mango and physalis"/>
    <!-- curved lime swoosh edging the photo -->
    <path d="M300 150 Q520 260 720 612 L760 612 Q560 240 330 160 Z" fill="var(--white)"/>
    <path d="M310 152 Q530 255 735 612 L752 612 Q550 245 325 158 Z" fill="var(--lime)"/>
    <!-- headline band -->
    <path d="M330 160 L1044 160 L1044 306 L448 306 Q400 220 330 160 Z" fill="var(--white)"/>
    <path d="M345 166 L1044 166 L1044 300 L452 300 Q405 225 345 166 Z" fill="var(--lime)"/>
    <!-- info band -->
    <rect x="700" y="482" width="344" height="108" fill="var(--white)"/>
    <rect x="706" y="488" width="338" height="96" fill="var(--lime)"/>
    <!-- bottom band -->
    <rect x="0" y="612" width="806" height="132" fill="var(--lime)"/>
    <path d="M720 612 L806 612 L806 600 Z" fill="var(--lime-dark)"/>
    <!-- dashed rules -->
    <g stroke="var(--ink)" stroke-width="1.5" stroke-dasharray="6 5" fill="none" opacity=".8">
      <line x1="0" y1="60" x2="110" y2="75"/>
      <line x1="330" y1="136" x2="1044" y2="136"/>
      <line x1="540" y1="322" x2="1044" y2="322"/>
      <path d="M440 306 Q560 420 680 612"/>
    </g>
  </svg>

  <div class="brand">
    <div class="brand-circle"></div>
    <div class="brand-name">Our Kitchen Pantry</div>
  </div>

  <div class="script headline-top">Be a part of our</div>

  <div class="pitch pitch-lead">Exciting new online food marketplace</div>
  <div class="pitch pitch-big">Connecting foodies</div>
  <div class="pitch pitch-tail">In your local community</div>

  <p class="about">As a food lover you can purchase lovingly grown or prepared food and support your local foodie community while keeping your food miles low</p>

  <div class="info">
    <div class="info-label">For more information</div>
    <div class="info-web">www.ourkitchenpantrynz.co.nz</div>
  </div>

  <div class="script headline-foodie">As a foodie</div>

  <div class="sell">
    <div class="sell-lead">You can sell your beautiful home produced</div>
    <div class="sell-tail">or home grown produce on our marketplace website</div>
  </div>

  <div class="contact">
    <div class="contact-label">Call us today</div>
    <div class="contact-phone">0800 555 0142</div>
  </div>
</div>
</body>
</html>
```